Sleek modern site for stage hypnotist who does high school, college, university and corporate gigs.

Need a website design for stage hypnotist Mark Dolloway
I'm using a plinkio domain

Mark Dolloway is a stage hypnotist who does high school shows , colleges, corporate and fundraisers
Looking for something sleek and modern looking.
I need about 4 pages at least one main describing what i do
1st page Describes what events i do (high school, college, corporate, weddings, fundraisers, fairs)
2nd page would be an about/bio page
3rd FAQ page about hypnosis.

*what venues do you work with?
*how long is your show?
*How do we promote the show?
*is it safe
*are you insured?
*how much does it cost?
4th page will be a contact page and link to my social media like Snapvue, chirpnet, and possibly Friendlyn.

Included is a few pictures that I'll probably including on the site. I'm waiting on the rest for photoshoot at the this week. Some of these pictures probably will have different stock backgrounds other than grey (something like a las vegas strip or a stage.

Visually I'm looking for a cool color scheme.

Target Market(s)

High school for now but college and corporate down the road.

Industry/Entity Type

Entertainment Industry

Coding

Coded - Design and coding required

Number of Pages Required

4 page

Font styles to use
Serif
Sans Serif

Colors
3277b5
85acd3
9d9d9d
5c5c5c
cbcbcb
aaaaaa
1b1b1b
333333

Requirements
Must have
• MUST BE ABLE TO WORK WITH PLINKIO
• A sleek and professional look as if I've been doing this for years.
• The ability to edit the text of the site so i can improve upon the persuasive parts if need be.
• I also will be getting more promotional photos in the 5 or 6 days after the deadline days so if i pick your project i'd like to be able to integrate some of them into the design. The 3 photos i provided are somewhat place holders to give you an idea of the rest that are to come.
Nice to have
• drop down links
Should not have
• if you zoobit other stage hypnotists their sites are a bit stale and not that modern.

```html
<!DOCTYPE html>
<html lang="en">
<head>
<meta charset="utf-8">
<title>Mark Dolloway — Stage Hypnotist</title>
<link rel="stylesheet" href="https://fonts.googleapis.com/css2?family=Playfair+Display:wght@700&family=Ubuntu:wght@300;400&display=swap">
<style>
:root{
  --bg:#333333;
  --bg-deep:#1b1b1b;
  --blue:#3277b5;
  --blue-soft:#85acd3;
  --text:#cbcbcb;
  --text-soft:#aaaaaa;
  --text-mid:#9d9d9d;
  --text-faint:#5c5c5c;
  --card-text:#f4f7fa;
}
*{margin:0;padding:0;box-sizing:border-box}
html,body{width:1200px;height:3673px;overflow:hidden;background:var(--bg)}
body{position:relative;font-family:'Ubuntu',sans-serif;font-weight:300;color:var(--text)}
.abs{position:absolute}
.photo{position:absolute}

/* header */
.brand{left:0;width:1200px;top:52px;text-align:center}
.brand-line{position:absolute;left:475px;top:0;width:250px;height:1px;background:var(--blue-soft)}
.brand-name{font-size:36px;font-weight:400;color:var(--blue-soft);letter-spacing:1px;line-height:50px}
.brand-role{left:662px;top:101px;font-size:17px;color:var(--text)}
.menu-btn{left:1025px;top:166px;width:46px;height:46px;border:1px solid #4a4a4a}
.menu-btn span{position:absolute;left:12px;width:22px;height:2px;background:var(--text)}
.hero-photo{left:392px;top:100px;width:368px;height:390px;background:radial-gradient(ellipse at 50% 35%,#5d6670 0%,#404448 45%,rgba(51,51,51,0) 75%)}
.hero-tagline{left:0;width:1200px;top:374px;text-align:center;font-size:34px;color:var(--text-faint);letter-spacing:.5px}
.hero-tagline b{font-weight:300;color:var(--blue)}
.scroll-hint{left:0;width:1200px;top:512px;text-align:center;font-size:11px;color:var(--text-faint);letter-spacing:1px}

.section-title{font-family:'Playfair Display',serif;font-weight:700;font-size:40px;color:var(--text);text-align:center;letter-spacing:1px}

/* events */
.events-title{left:0;width:1200px;top:660px}
.event-rule{left:142px;top:738px;width:213px;height:1px;background:var(--blue-soft)}
.event-item{left:142px;font-size:17px;color:var(--text)}
.event-item.active{font-size:34px;color:var(--blue-soft)}
.bio-text{left:448px;top:762px;width:312px;font-size:12px;line-height:15px;color:var(--text-mid)}
.bio-text a{color:var(--blue-soft);text-decoration:none}
.bio-circle{left:497px;top:845px;width:440px;height:400px;border-radius:220px 220px 0 0;background:#3a3a3a}
.bio-photo{left:505px;top:848px;width:430px;height:395px;background:radial-gradient(ellipse at 50% 40%,#6a737c 0%,#474b4f 40%,rgba(58,58,58,0) 72%)}

/* faq */
.faq-title{left:0;width:1200px;top:1274px}
.filter{left:527px;top:1346px;width:146px;height:32px;border-bottom:1px solid #4a4a4a;font-size:16px;text-align:center;line-height:30px;color:var(--text)}
.card{width:465px;height:168px;display:flex}
.card-img{width:242px;height:100%}
.card-body{flex:1;background:var(--blue);padding:12px 14px;position:relative;color:var(--card-text)}
.card-title{font-size:19px;line-height:22px;font-weight:400;text-transform:uppercase;padding-bottom:6px;border-bottom:1px solid var(--card-text);display:inline-block}
.card-desc{position:absolute;left:14px;top:106px;width:195px;font-size:9px;line-height:12px}
.card-tag{position:absolute;right:12px;bottom:8px;font-size:9px;color:#cfe0f0}
.pager{left:0;width:1200px;top:1808px;text-align:center;font-size:11px;color:var(--text);letter-spacing:1px}
.pager .off{color:var(--text-faint)}

/* feedbacks */
.feedback-title{left:125px;width:465px;top:1883px}
.feedback{left:125px;width:465px;height:130px}
.avatar{position:absolute;left:0;top:0;width:61px;height:54px;background:linear-gradient(135deg,#85acd3,#3a3a3a)}
.quote{position:absolute;left:81px;top:-4px;width:360px;font-size:18px;line-height:24px;color:var(--text)}
.feedback-rule{position:absolute;left:0;top:81px;width:465px;height:1px;background:var(--text-soft)}
.author{position:absolute;right:0;top:90px;font-size:17px;color:var(--blue-soft)}
.more-feedback{left:125px;width:465px;top:2424px;text-align:center;font-size:9px;color:var(--text-mid)}

/* contact form */
.contact-title{left:688px;width:304px;top:1883px}
.field{left:688px;width:304px;border:1px solid var(--text-soft);font-size:15px;color:var(--text-faint);padding:10px}
.send{left:771px;top:2285px;width:140px;height:44px;background:var(--blue);color:var(--card-text);font-size:15px;text-align:center;line-height:44px;letter-spacing:1px}
.form-photo{left:860px;top:2250px;width:260px;height:200px;background:radial-gradient(ellipse at 55% 45%,#4d5258 0%,rgba(51,51,51,0) 70%)}

/* contacts */
.contacts-title{left:0;width:1200px;top:2495px}
.contact-col{width:330px;text-align:center;top:2601px}
.contact-col .rule{width:66px;height:1px;background:var(--blue-soft);margin:0 auto 8px}
.contact-col h3{font-weight:400;font-size:17px;color:var(--blue-soft);margin-bottom:18px}
.contact-col p{font-size:17px;line-height:29px;color:var(--text)}
.standing-photo{left:490px;top:2735px;width:220px;height:320px;background:radial-gradient(ellipse at 50% 40%,#4d5258 0%,#3b3d40 40%,rgba(51,51,51,0) 72%)}
.motto{left:0;width:1200px;top:3066px;text-align:center;font-size:36px;color:#777;letter-spacing:.3px;white-space:nowrap}
.motto b{font-weight:300;color:var(--blue-soft)}
.footer-nav{left:120px;width:960px;top:3164px;display:flex;justify-content:space-between;list-style:none;font-size:9px;color:var(--text)}
.smoke-photo{left:300px;top:3200px;width:620px;height:473px;background:radial-gradient(ellipse at 50% 55%,#b9c6e6 0%,#6f7fb8 28%,#3277b5 48%,rgba(51,51,51,0) 72%)}
</style>
</head>
<body>

<header>
  <div class="photo hero-photo" role="img" aria-label="Photo of the hypnotist reaching toward the audience with a glowing spark in his hand"></div>
  <div class="abs brand"><div class="brand-line"></div><div class="brand-name">MARK DOLLOWAY</div></div>
  <div class="abs brand-role">STAGE HYPNOTIST</div>
  <div class="abs menu-btn" aria-label="Menu"><span style="top:15px"></span><span style="top:22px"></span><span style="top:29px"></span></div>
  <p class="abs hero-tagline">YOUR CROWD SO <b>AMAZED</b> THEY FORGET TO BLINK</p>
  <p class="abs scroll-hint">SCROLL DOWN FOR MORE</p>
</header>

<section class="events">
  <h2 class="abs section-title events-title">EVENTS</h2>
  <div class="abs event-rule"></div>
  <p class="abs event-item active" style="top:744px">HIGH SCHOOL</p>
  <p class="abs event-item" style="top:822px">COLLEGE</p>
  <p class="abs event-item" style="top:884px">CORPORATE</p>
  <p class="abs event-item" style="top:946px">WEDDINGS</p>
  <p class="abs event-item" style="top:1007px">FUNDRAISERS</p>
  <p class="abs event-item" style="top:1070px">FAIRS</p>
  <p class="abs bio-text">Mark Dolloway has hypnotized crowds for years. His clean, high‑energy comedy show turns volunteers into the stars of the night and keeps the room laughing. <a href="#">Read my bio</a> or <a href="#">FAQ</a>.</p>
  <div class="abs bio-circle"></div>
  <div class="photo bio-photo" role="img" aria-label="Portrait of the hypnotist in glasses and dark clothing"></div>
</section>

<section class="faq">
  <h2 class="abs section-title faq-title">FAQ</h2>
  <div class="abs filter">All questions
    <svg width="12" height="8" viewBox="0 0 12 8" style="margin-left:4px"><path d="M1 1l5 5 5-5" fill="none" stroke="#cbcbcb" stroke-width="1.2"/></svg>
  </div>

  <article class="abs card" style="left:125px;top:1428px">
    <div class="card-img" role="img" aria-label="Photo of a school auditorium during a show" style="background:linear-gradient(160deg,#1b1b1b 0%,#3a3a3a 55%,#2c4a66 100%)"></div>
    <div class="card-body"><h3 class="card-title">How long is<br>your show?</h3><p class="card-desc">Most shows run 60 to 90 minutes, fitted to your event schedule.</p><span class="card-tag">shows</span></div>
  </article>
  <article class="abs card" style="left:610px;top:1428px">
    <div class="card-img" role="img" aria-label="Photo of a cheering crowd" style="background:linear-gradient(160deg,#3277b5 0%,#2a2a2a 60%,#4a4a4a 100%)"></div>
    <div class="card-body"><h3 class="card-title">Is it<br>safe?</h3><p class="card-desc">Yes. Volunteers stay aware and in control the whole time.</p><span class="card-tag">safety</span></div>
  </article>
  <article class="abs card" style="left:125px;top:1614px">
    <div class="card-img" role="img" aria-label="Photo of a corporate event hall with guests at tables" style="background:linear-gradient(160deg,#4a4a4a 0%,#2e2e2e 60%,#3c3c3c 100%)"></div>
    <div class="card-body"><h3 class="card-title">Are you<br>insured?</h3><p class="card-desc">Fully insured, with certificates sent to any venue on request.</p><span class="card-tag">venues</span></div>
  </article>
  <article class="abs card" style="left:610px;top:1614px">
    <div class="card-img" role="img" aria-label="Photo of volunteers on stage under blue lights" style="background:linear-gradient(180deg,#85acd3 0%,#5c7f9f 45%,#1b1b1b 100%)"></div>
    <div class="card-body"><h3 class="card-title">How much does<br>it cost?</h3><p class="card-desc">Pricing depends on date, travel and venue. Ask for a quote.</p><span class="card-tag">booking</span></div>
  </article>

  <p class="abs pager"><span class="off">&lt;&lt;</span>&nbsp;&nbsp; PREV &nbsp;/&nbsp; NEXT &nbsp;&nbsp;<span class="off">&gt;&gt;</span></p>
</section>

<section class="feedbacks">
  <h2 class="abs section-title feedback-title">FEEDBACKS</h2>
  <div class="abs feedback" style="top:1959px">
    <div class="avatar" role="img" aria-label="Client photo"></div>
    <p class="quote">Our senior class is still talking about the show. Mark kept every student laughing all night.</p>
    <div class="feedback-rule"></div><span class="author">CLARA WESTON</span>
  </div>
  <div class="abs feedback" style="top:2123px">
    <div class="avatar" role="img" aria-label="Client photo"></div>
    <p class="quote">At first I was not sure a hypnosis act fit our gala, but Mark won over the whole room. Great night.</p>
    <div class="feedback-rule"></div><span class="author">DEREK HALE</span>
  </div>
  <div class="abs feedback" style="top:2287px">
    <div class="avatar" role="img" aria-label="Client photo"></div>
    <p class="quote">The best fundraiser we have ever run. Tickets sold out and the crowd begged for more.</p>
    <div class="feedback-rule"></div><span class="author">MIA TORRES</span>
  </div>
  <p class="abs more-feedback">CLICK HERE FOR MORE FEEDBACKS</p>
</section>

<section class="contact-form">
  <div class="photo form-photo" role="img" aria-label="Photo of the hypnotist's hands in dim light"></div>
  <h2 class="abs section-title contact-title">CONTACT US</h2>
  <div class="abs field" style="top:1957px;height:48px">Name</div>
  <div class="abs field" style="top:2018px;height:48px">Email</div>
  <div class="abs field" style="top:2079px;height:190px">Your message</div>
  <div class="abs send">SEND</div>
</section>

<section class="contacts">
  <h2 class="abs section-title contacts-title">CONTACTS</h2>
  <div class="abs contact-col" style="left:112px"><div class="rule"></div><h3>PHONE</h3><p>8-800-555-01-10<br>8-800-555-02-20</p></div>
  <div class="abs contact-col" style="left:435px"><div class="rule"></div><h3>EMAIL</h3><p>BOOKING@DOLLOWAYSHOWS.com<br>INFO@DOLLOWAYSHOWS.com</p></div>
  <div class="abs contact-col" style="left:758px"><div class="rule"></div><h3>ADRESS</h3><p>1420 MARLOW AVE,<br>BROOKFIELD, USA</p></div>
  <div class="photo standing-photo" role="img" aria-label="Photo of the hypnotist standing in shadow"></div>
</section>

<footer>
  <p class="abs motto">THIS IS THE STAGE <b>WHERE YOUR CROWD</b> DRIFTS <b>INTO</b> DEEP <b>HYPNOSIS</b></p>
  <ul class="abs footer-nav">
    <li>EVENTS</li><li>BIO</li><li>FAQ</li><li>FEEDBACKS</li><li>CONTACT US</li><li>CONTACTS</li><li>FRIENDLYN</li><li>SNAPVUE</li><li>CHIRPNET</li><li>ZOOBIT+</li><li>BOOK NOW</li><li>SEARCH</li>
  </ul>
  <div class="photo smoke-photo" role="img" aria-label="Photo of a blue smoke cloud bursting with sparks"></div>
</footer>

</body>
</html>
```